Lanternway 7.5 - Educational Guide/Course-pack/Worksheet

Our Lanternway 7.5 toolkit is an educational workshop that focuses on inspiring student initiatives in the classroom! We need a new educational course guide or course-pack for students/teachers that clearly outlines or explains the program steps, offers helpful tips and includes empty spaces/lines where their can write down their great ideas or notes. This will include a;

- Teachers Guide (1 Page)
- Student Guide/Worksheet (4 Pages)
- Group Pack Resources (3 Pages)

This will consist of designing/formatting text, stock animation/icons, font, etc. We have included our new logo (color, branding, etc.) and all of the text for each separate course-pack. We have also attached our new website to give you an idea of the program style.

Our workshop can be for any school project like Technology, Community, Environment, Art, Science, etc.

Target Market(s)

High School Students/Teachers

Industry/Entity Type

Education

Font styles to use
Sans Serif

Colors
f68e4e
acd037
34a7d8

Requirements
Must have
• Use our brand colors from logo.
Should not have
• Should not be too childish.

```html
<!DOCTYPE html>
<html lang="en">
<head>
<meta charset="utf-8">
<title>Lanternway 7.5 – Me and We Worksheet</title>
<link href="https://fonts.googleapis.com/css2?family=Roboto+Condensed:wght@300;400;700&display=swap" rel="stylesheet">
<style>
  :root {
    --ink: #111111;
    --text: #1d1d1d;
    --brand-grey: #6d6e70;
    --rule-faint: #ececec;
    --orange: #f68e4e;
    --green: #acd037;
    --blue: #34a7d8;
    --paper: #ffffff;
  }
  * { margin: 0; padding: 0; box-sizing: border-box; }
  html, body { width: 928px; height: 1200px; overflow: hidden; background: var(--paper); }
  .sheet {
    position: relative;
    width: 928px; height: 1200px;
    border: 1px solid var(--ink);
    font-family: "Roboto Condensed", "Arial Narrow", sans-serif;
    color: var(--text);
  }
  .brand { position: absolute; left: 44px; top: 46px; display: flex; align-items: center; gap: 22px; }
  .brand-mark { width: 62px; height: 62px; border-radius: 50%; background: var(--blue); }
  .brand-name { font-weight: 400; font-size: 40px; color: var(--brand-grey); line-height: 1; }
  .brand-tagline { font-weight: 400; font-size: 16px; color: var(--brand-grey); margin-top: 6px; letter-spacing: 0.3px; }
  .brand-rule { position: absolute; left: 42px; top: 154px; width: 322px; height: 1px; background: var(--rule-faint); }

  .section-title { position: absolute; left: 50px; top: 174px; font-weight: 700; font-size: 25px; color: var(--ink); }

  .block-icon { position: absolute; left: 42px; width: 50px; border-radius: 8px; }
  .icon-me { top: 237px; height: 40px; background: linear-gradient(135deg, #d9e4ea, var(--green)); }
  .icon-we { top: 468px; height: 54px; background: linear-gradient(135deg, var(--blue), #f6c34e 60%, var(--orange)); opacity: 0.55; }

  .block { position: absolute; left: 110px; width: 660px; }
  .block h2 { font-weight: 700; font-size: 20px; color: var(--ink); line-height: 1.2; }
  .block p { font-weight: 300; font-size: 17px; line-height: 22px; margin-top: 2px; }
  .block-me { top: 237px; }
  .block-we { top: 480px; }

  .write-line { position: absolute; height: 1.6px; width: 316px; background: var(--ink); }

  .member-card {
    position: absolute; width: 316px; height: 204px;
    border: 1.5px solid var(--ink); border-radius: 33px;
    padding: 22px 0 0 22px;
    font-weight: 300; font-size: 15px;
  }
</style>
</head>
<body>
<main class="sheet">
  <header class="brand">
    <span class="brand-mark" aria-hidden="true"></span>
    <div>
      <div class="brand-name">Lanternway 7.5</div>
      <div class="brand-tagline">Spark · Build · Learn</div>
    </div>
  </header>
  <div class="brand-rule"></div>

  <h1 class="section-title">1.&nbsp; Me and We</h1>

  <div class="block-icon icon-me" role="img" aria-label="Icon of a strong person with an upward arrow"></div>
  <section class="block block-me">
    <h2>Me</h2>
    <p>List some of your talents abilities, and interests.<br>
    Think about private classes, sports, hobbies, music, computers, things you like, things you know how to do.</p>
  </section>

  <div class="write-line" style="left:110px;top:356px"></div>
  <div class="write-line" style="left:450px;top:356px"></div>
  <div class="write-line" style="left:110px;top:385px"></div>
  <div class="write-line" style="left:450px;top:385px"></div>
  <div class="write-line" style="left:110px;top:414px"></div>
  <div class="write-line" style="left:450px;top:414px"></div>
  <div class="write-line" style="left:110px;top:443px"></div>
  <div class="write-line" style="left:450px;top:443px"></div>

  <div class="block-icon icon-we" role="img" aria-label="Icon of three people around a speech bubble"></div>
  <section class="block block-we">
    <h2>We</h2>
    <p>List the talents, abilities, and interests of each of your group members.</p>
  </section>

  <div class="member-card" style="left:110px;top:631px">Name:</div>
  <div class="member-card" style="left:450px;top:627px">Name:</div>
  <div class="member-card" style="left:110px;top:858px">Name:</div>
  <div class="member-card" style="left:450px;top:858px">Name:</div>
</main>
</body>
</html>
```